Marta Business Card

My wife is going to start her own business with renting holiday appartments to tourists. She needs a design for a new business card... and a new web site.
Look at Stayvolt "Erholung auf dem Lindenwäldchen"

Target Market(s)

Give business card to prospects at any situation

Contact Information for Business Card

not sure what this means

Font styles to use
Script

Colors
fec41a
fee18a

Requirements
Must have
• My wife's handwriting is difficult to read:
Entspannen - Loslassen - Auftanken
Marta & das Lindenwäldchen
Urlaub an einem besonderen Ort
Marta Brecke
Grauer Pfad 7
18471 Alt Feldow
post@marta-brecke.de
www.lindenwaeldchen.net
Nice to have
• Beige background
Font like handwriting

```html
<!DOCTYPE html>
<html lang="de">
<head>
<meta charset="utf-8">
<title>Marta &amp; das Lindenwäldchen – Visitenkarte</title>
<link rel="stylesheet" href="https://fonts.googleapis.com/css2?family=Damion&display=swap">
<style>
  :root {
    --page-bg: #e7e8ea;
    --card-front: #ffffff;
    --card-back: #ede8e1;
    --pattern-front: #fbfaf8;
    --pattern-back: #f1ede7;
    --ink: #333132;
  }
  * { box-sizing: border-box; margin: 0; padding: 0; }
  html, body {
    width: 1200px;
    height: 1195px;
    overflow: hidden;
    background: var(--page-bg);
  }
  body {
    display: flex;
    flex-direction: column;
    align-items: center;
    justify-content: center;
    gap: 60px;
    font-family: "Damion", cursive;
    color: var(--ink);
  }
  .card {
    position: relative;
    width: 880px;
    height: 455px;
    overflow: hidden;
    box-shadow: 0 10px 30px rgba(0,0,0,0.08);
  }
  .card--front { background: var(--card-front); }
  .card--back { background: var(--card-back); }
  .card__pattern {
    position: absolute;
    inset: 0;
  }
  .card--front .card__pattern { background: var(--pattern-front); }
  .card--back .card__pattern { background: linear-gradient(135deg, var(--card-back), var(--pattern-back)); }
  .card__content {
    position: relative;
    height: 100%;
  }
  .card--front .card__content {
    display: flex;
    align-items: center;
    justify-content: center;
  }
  .brand-name {
    font-weight: 400;
    font-size: 56px;
    letter-spacing: 1px;
    line-height: 1;
  }
  .card--back .brand-block {
    position: absolute;
    top: 145px;
    left: 0;
    right: 0;
    text-align: center;
  }
  .card--back .brand-name { font-size: 50px; margin: 10px 0 12px; }
  .motto { font-size: 24px; letter-spacing: 1px; }
  .subline { font-size: 27px; letter-spacing: 1px; }
  .contact {
    position: absolute;
    bottom: 52px;
    font-size: 17px;
    line-height: 1.65;
    font-style: normal;
  }
  .contact--address { left: 105px; }
  .contact--online { right: 105px; bottom: 44px; }
</style>
</head>
<body>
  <section class="card card--front">
    <div class="card__pattern" role="img" aria-label="Feines Streumuster aus hellen, kurzen Strichen"></div>
    <div class="card__content">
      <h1 class="brand-name">Marta &amp; das Lindenwäldchen</h1>
    </div>
  </section>

  <section class="card card--back">
    <div class="card__pattern" role="img" aria-label="Feines Streumuster aus hellen, kurzen Strichen auf Beige"></div>
    <div class="card__content">
      <div class="brand-block">
        <p class="motto">Entspannen – Loslassen – Auftanken</p>
        <h2 class="brand-name">Marta &amp; das Lindenwäldchen</h2>
        <p class="subline">Urlaub an einem besonderen Ort</p>
      </div>
      <address class="contact contact--address">
        Marta Brecke<br>
        Grauer Pfad 7<br>
        18471 Alt Feldow
      </address>
      <address class="contact contact--online">
        post@marta-brecke.de<br>
        www.lindenwaeldchen.net
      </address>
    </div>
  </section>
</body>
</html>
```